Business Card Design

I need a Business Card that will catch the attention that will not get thrown in a Drawer. I have 23 companies I use for Auto, Home, Life, and Business Insurance. I make sure that people have the best coverage for the $ spent.

Industry/Entity Type

Business

Contact Information for Business Card

Dorlin Insurance Agency, Inc., Marcus Helgren, 4375 West Tamber Lane Brantwick, Orland 45192 555-281-7496, www.dorlinagency.example, Friendlink, Workmesh, Circleplus

```html
<!DOCTYPE html>
<html lang="en">
<head>
<meta charset="utf-8">
<title>Dorlin Insurance Agency – Business Card</title>
<link rel="stylesheet" href="https://fonts.googleapis.com/css2?family=Didact+Gothic&family=Montserrat:wght@700&family=Raleway:wght@200&display=swap">
<style>
  :root {
    --backdrop: #ecebe8;
    --card-green: #12876a;
    --ink-white: #ffffff;
    --name-cyan: #22b4d8;
    --url-blush: #f1b9b4;
    --rule: rgba(255, 255, 255, 0.85);
    --chip: rgba(255, 255, 255, 0.9);
  }
  * { box-sizing: border-box; margin: 0; padding: 0; }
  html, body {
    width: 1200px;
    height: 938px;
    overflow: hidden;
    background: var(--backdrop);
  }
  .stage {
    width: 1200px;
    height: 938px;
    display: flex;
    align-items: center;
    justify-content: center;
  }
  .business-card {
    position: relative;
    width: 500px;
    height: 860px;
    background: var(--card-green);
    box-shadow: 0 10px 30px rgba(0, 0, 0, 0.18);
    padding: 70px 56px 60px;
    display: flex;
    flex-direction: column;
  }
  .agency-name {
    font-family: "Raleway", sans-serif;
    font-weight: 200;
    font-size: 66px;
    line-height: 1.12;
    letter-spacing: 2px;
    color: var(--ink-white);
    text-transform: uppercase;
  }
  .agency-name span { display: block; }
  .divider {
    margin: 44px 0 40px auto;
    width: 340px;
    height: 1px;
    background: var(--rule);
  }
  .contact {
    font-style: normal;
    text-align: right;
    color: var(--ink-white);
    font-family: "Didact Gothic", sans-serif;
  }
  .agent-name {
    font-family: "Montserrat", sans-serif;
    font-weight: 700;
    font-size: 36px;
    letter-spacing: 1px;
    color: var(--name-cyan);
    text-transform: uppercase;
    margin-bottom: 14px;
  }
  .contact-line {
    font-size: 31px;
    line-height: 1.3;
    white-space: nowrap;
  }
  .website {
    margin-top: 10px;
    font-size: 22px;
    color: var(--url-blush);
  }
  .social-list {
    margin-top: auto;
    list-style: none;
    display: flex;
    flex-direction: column;
    align-items: flex-end;
    gap: 14px;
    font-family: "Didact Gothic", sans-serif;
    font-size: 20px;
    color: var(--ink-white);
  }
  .social-item {
    display: flex;
    align-items: center;
    gap: 10px;
  }
  .social-chip {
    width: 14px;
    height: 14px;
    background: var(--chip);
  }
</style>
</head>
<body>
  <main class="stage">
    <article class="business-card">
      <h1 class="agency-name">
        <span>Dorlin</span>
        <span>Insurance</span>
        <span>Agency</span>
      </h1>
      <div class="divider"></div>
      <address class="contact">
        <p class="agent-name">Marcus Helgren</p>
        <p class="contact-line">45192 555-281-7496</p>
        <p class="contact-line">4375 West Tamber Lane</p>
        <p class="contact-line">Brantwick, Orland</p>
        <p class="website">www.dorlinagency.example</p>
      </address>
      <ul class="social-list">
        <li class="social-item"><span class="social-chip"></span>Circleplus</li>
        <li class="social-item"><span class="social-chip"></span>Workmesh</li>
        <li class="social-item"><span class="social-chip"></span>Friendlink</li>
      </ul>
    </article>
  </main>
</body>
</html>
```